Quiet Lanterns: Reflections on Tide Charts and Orchard Rituals Among Coastal Villages.

Book cover, spine, and back cover. This is written by Dr. T. HALVERSEN, and will be an educational book for academics, government officials, and the general population.
I'm imagining the outline of a person with am active mind in the middle. It would be overlayed on top of a circular galaxy on the background. On either side, smaller, perhaps in the background would be a cross on one side and a few uaps (ufo) of different shapes on the other (orb, saucer, triangle. ) beneath allnof this would be something symbolizing society - either the earth itself or the skyline of a large city.
By Dr. T. HALVERSEN along the bottom, i presume. (Ai cannot make this, but I've included a few examples nonetheless. )
I assume I will be given the opportunity to write a synopsis on the back cover. I will be self publishing and selling from my website.
Target Market(s)
Academics, professionals, church leaders, government officials, and the general public.
Industry/Entity Type
Professional and community education
Requirements
Must have
- It should look like a ph.d level book. Eye catching but not overly fantastical. (Its an educational book not a comic book)
Should not have
- Not hollywood or fantasy book looking. It should look a graduate school book. The tone is quite serious.

```html
<!DOCTYPE html>
<html lang="en">
<head>
<meta charset="utf-8">
<title>Quiet Lanterns — Cover Spread</title>
<link rel="stylesheet" href="https://fonts.googleapis.com/css2?family=Cinzel:wght@500;600&family=Forum&family=Montserrat:wght@600;700&display=swap">
<style>
  :root {
    --page: #ffffff;
    --nebula-deep: #2c3f7c;
    --nebula-blue: #4a78c2;
    --nebula-sky: #7fb6e6;
    --nebula-violet: #7a5690;
    --nebula-rose: #b7687a;
    --nebula-amber: #e8a36a;
    --title-cream: #f4e8d8;
    --subtitle-white: #f7f3f1;
    --author-navy: #1d2553;
    --spine-author: #ffffff;
    --glow-core: #f7d9e8;
    --glow-blue: #3d6fd0;
  }
  * { margin: 0; padding: 0; box-sizing: border-box; }
  html, body {
    width: 1200px;
    height: 1200px;
    overflow: hidden;
    background: var(--page);
  }
  .spread {
    position: absolute;
    left: 131px;
    top: 260px;
    width: 935px;
    height: 677px;
    overflow: hidden;
    box-shadow: 0 14px 28px rgba(0, 0, 0, 0.28);
  }
  .nebula-artwork {
    position: absolute;
    inset: 0;
    background:
      radial-gradient(ellipse 30% 22% at 50% 46%, rgba(255, 240, 230, 0.55), transparent 70%),
      radial-gradient(ellipse 55% 40% at 22% 12%, rgba(232, 163, 106, 0.55), transparent 70%),
      radial-gradient(ellipse 45% 35% at 80% 10%, rgba(232, 163, 106, 0.45), transparent 70%),
      radial-gradient(ellipse 40% 30% at 12% 92%, rgba(232, 163, 106, 0.7), transparent 70%),
      radial-gradient(ellipse 50% 40% at 35% 45%, rgba(122, 86, 144, 0.7), transparent 70%),
      radial-gradient(ellipse 55% 45% at 70% 30%, rgba(127, 182, 230, 0.65), transparent 70%),
      radial-gradient(ellipse 40% 40% at 45% 80%, rgba(183, 104, 122, 0.55), transparent 70%),
      linear-gradient(160deg, var(--nebula-violet), var(--nebula-blue) 45%, var(--nebula-deep) 70%, var(--nebula-violet));
  }
  .horizon-line {
    position: absolute;
    left: 0;
    right: 0;
    top: 349px;
    height: 2px;
    background: linear-gradient(90deg, transparent, rgba(255, 255, 255, 0.6) 30%, rgba(255, 255, 255, 0.75) 55%, transparent);
  }
  .back-cover, .spine, .front-cover {
    position: absolute;
    top: 0;
    height: 100%;
  }
  .back-cover { left: 0; width: 431px; }
  .spine { left: 431px; width: 71px; }
  .front-cover { left: 502px; width: 433px; }

  .title {
    font-family: "Cinzel", serif;
    font-weight: 600;
    color: var(--title-cream);
    text-align: center;
    line-height: 1.02;
    text-shadow: 0 2px 6px rgba(30, 30, 70, 0.35);
  }
  .subtitle {
    font-family: "Forum", serif;
    color: var(--subtitle-white);
    text-align: center;
    text-transform: uppercase;
    line-height: 1.2;
  }
  .back-cover .title {
    position: absolute;
    top: 54px;
    left: 0;
    width: 100%;
    font-size: 42px;
  }
  .back-cover .subtitle {
    position: absolute;
    top: 148px;
    left: 50px;
    width: 331px;
    font-size: 13px;
  }
  .front-cover .title {
    position: absolute;
    top: 66px;
    left: 0;
    width: 100%;
    font-size: 58px;
  }
  .front-cover .subtitle {
    position: absolute;
    top: 210px;
    left: 55px;
    width: 323px;
    font-size: 16px;
  }
  .cosmic-mind-artwork {
    position: absolute;
    left: 60px;
    top: 262px;
    width: 380px;
    height: 330px;
    border-radius: 50%;
    background:
      radial-gradient(circle at 45% 30%, var(--glow-core) 0 10%, rgba(233, 140, 190, 0.7) 16%, transparent 32%),
      radial-gradient(ellipse 60% 40% at 50% 55%, rgba(61, 111, 208, 0.95), rgba(40, 70, 170, 0.6) 60%, transparent 80%),
      radial-gradient(ellipse 70% 55% at 50% 55%, rgba(90, 140, 230, 0.5), transparent 75%);
  }
  .author {
    position: absolute;
    top: 609px;
    left: 0;
    width: 100%;
    text-align: center;
    font-family: "Montserrat", sans-serif;
    font-weight: 700;
    font-size: 20px;
    color: var(--author-navy);
    letter-spacing: 0.5px;
  }
  .spine-title {
    position: absolute;
    top: 140px;
    left: 50%;
    transform: translateX(-50%);
    writing-mode: vertical-rl;
    font-family: "Cinzel", serif;
    font-weight: 600;
    font-size: 33px;
    color: var(--title-cream);
    white-space: nowrap;
    text-shadow: 0 2px 6px rgba(30, 30, 70, 0.35);
  }
  .spine-author {
    position: absolute;
    top: 512px;
    left: 50%;
    transform: translateX(-50%);
    writing-mode: vertical-rl;
    font-family: "Montserrat", sans-serif;
    font-weight: 700;
    font-size: 13px;
    color: var(--spine-author);
    white-space: nowrap;
    letter-spacing: 0.5px;
  }
</style>
</head>
<body>
  <div class="spread">
    <div class="nebula-artwork" role="img" aria-label="Nebula starfield artwork in violet, blue and amber spanning the full cover"></div>
    <div class="horizon-line"></div>

    <section class="back-cover">
      <h2 class="title">QUIET<br>LANTERNS</h2>
      <p class="subtitle">Reflections on Tide Charts and Orchard Rituals Among Coastal Villages</p>
    </section>

    <section class="spine">
      <span class="spine-title">QUIET LANTERNS</span>
      <span class="spine-author">Dr. T. HALVERSEN</span>
    </section>

    <section class="front-cover">
      <h1 class="title">QUIET<br>LANTERNS</h1>
      <p class="subtitle">Reflections on Tide Charts and Orchard Rituals Among Coastal Villages</p>
      <div class="cosmic-mind-artwork" role="img" aria-label="Illustration of a glowing human head outline over an orbital galaxy, with a small cross, planets and flying craft"></div>
      <p class="author">Dr. T. HALVERSEN</p>
    </section>
  </div>
</body>
</html>
```